Property Developer Business card design

we need a business card design + printing for a new Property developer company based in melbourne.
We are a group of investors investing in a property developer business. We have more projects involved in residential property as opposed to commercial property but we are involved in both market. we also provide consulting services with overseas investors willing to invest in the australian property market.
Updates
I have uploaded the logo. I'm not very convince with the colors of my logo... any suggestion please?.
Thanks guys!
Target Market(s)
property investors or person willing to purchase investment property
Industry/Entity Type
Residential
Contact Information for Business Card
Harbourne Capital Australia Pty Ltd
Look and feel
Each slider illustrates characteristics of the customer's brand and the style your logo design should communicate.

```html
<!DOCTYPE html>
<html lang="en">
<head>
<meta charset="utf-8">
<title>Harbourne Capital Australia – Business Card</title>
<link rel="stylesheet" href="https://fonts.googleapis.com/css2?family=Tinos:wght@400;700&family=Montserrat:wght@500&display=swap">
<style>
  :root {
    --canvas: #e4e4e4;
    --brand-blue: #0a78c2;
    --brand-red: #b01f2a;
    --paper: #ffffff;
    --ink-blue: #1e7fc7;
    --card-w: 600px;
    --card-h: 343px;
  }
  * { margin: 0; padding: 0; box-sizing: border-box; }
  html, body {
    width: 1200px; height: 985px; overflow: hidden;
    background: var(--canvas);
  }
  .stage { position: relative; width: 1200px; height: 985px; }
  .card {
    position: absolute;
    width: var(--card-w); height: var(--card-h);
    border-radius: 22px;
    overflow: hidden;
    background: var(--brand-blue);
    box-shadow: 0 6px 18px rgba(0,0,0,0.18);
  }
  .card--front { left: 300px; top: 95px; }
  .card--back  { left: 300px; top: 520px; }

  /* Front */
  .brand {
    font-family: "Tinos", serif;
    font-weight: 700;
    display: flex; align-items: center; gap: 10px;
  }
  .brand__dot { width: 16px; height: 16px; border-radius: 50%; }
  .card--front .brand {
    position: absolute; left: 0; right: 0; top: 110px;
    justify-content: center;
    color: var(--paper); font-size: 34px;
  }
  .card--front .brand__dot { background: var(--paper); }
  .company-line {
    position: absolute; left: 0; right: 0; top: 210px;
    text-align: center;
    font-family: "Tinos", serif; font-size: 25px;
    color: var(--paper); letter-spacing: 0.5px;
  }

  /* Back */
  .back-shape { position: absolute; inset: 0; }
  .card--back .brand {
    position: absolute; left: 40px; top: 48px;
    color: var(--ink-blue); font-size: 26px;
  }
  .card--back .brand__dot { background: var(--brand-red); }
  .person { position: absolute; left: 40px; top: 112px; font-family: "Tinos", serif; }
  .person__name { color: var(--brand-red); font-size: 30px; line-height: 1.1; }
  .person__title { color: var(--ink-blue); font-size: 19px; }

  .contact {
    position: absolute; right: 30px; bottom: 24px;
    text-align: right; color: var(--paper);
  }
  .contact__address {
    font-family: "Montserrat", sans-serif; font-weight: 500;
    font-variant: small-caps; font-size: 21px; line-height: 1.15;
    letter-spacing: 1px; margin-bottom: 8px;
  }
  .contact__row {
    display: flex; justify-content: flex-end; align-items: center; gap: 8px;
    font-family: "Montserrat", sans-serif; font-variant: small-caps;
    font-size: 13px; line-height: 1.35; letter-spacing: 0.5px;
  }
  .contact__email {
    display: flex; justify-content: flex-end; align-items: center; gap: 8px;
    font-family: "Tinos", serif; font-size: 18px; margin-top: 6px;
  }
  .icon { width: 16px; height: 16px; flex: none; }
</style>
</head>
<body>
<main class="stage">

  <section class="card card--front" aria-label="Card front">
    <div class="brand"><span class="brand__dot"></span>Harbourne Capital Australia</div>
    <p class="company-line">Harbourne Capital Australia Pty Ltd</p>
  </section>

  <section class="card card--back" aria-label="Card back">
    <svg class="back-shape" viewBox="0 0 600 343" preserveAspectRatio="none" aria-hidden="true">
      <path d="M0 0 H360 C470 0 480 150 425 205 C380 252 240 278 0 240 Z" fill="var(--brand-red)"/>
      <path d="M0 0 H330 C420 0 435 130 398 185 C360 240 250 262 0 226 Z" fill="var(--paper)"/>
    </svg>

    <div class="brand"><span class="brand__dot"></span>Harbourne Capital Australia</div>

    <div class="person">
      <p class="person__name">Daniel Marsh</p>
      <p class="person__title">Managing Director</p>
    </div>

    <div class="contact">
      <p class="contact__address">27 Saltbush Lane<br>Kinross VIC 3041</p>
      <div class="contact__row">
        <span>Telephone : +61 3 9000 1234<br>Mobile : 0400 555 210</span>
        <svg class="icon" viewBox="0 0 16 16" aria-hidden="true">
          <rect x="1" y="5" width="14" height="10" rx="2" fill="var(--brand-red)"/>
          <path d="M2 5 C2 1 14 1 14 5 L11 6 L11 4 C9 3 7 3 5 4 L5 6 Z" fill="var(--brand-red)"/>
          <circle cx="8" cy="10" r="2.5" fill="var(--brand-blue)"/>
        </svg>
      </div>
      <div class="contact__email">
        <span>daniel.marsh@harbournecapital.com.au</span>
        <svg class="icon" viewBox="0 0 16 16" aria-hidden="true">
          <rect x="1" y="3" width="14" height="10" fill="none" stroke="var(--brand-red)" stroke-width="1.4"/>
          <path d="M1 3 L8 9 L15 3 M1 13 L6 8 M15 13 L10 8" fill="none" stroke="var(--brand-red)" stroke-width="1.4"/>
        </svg>
      </div>
    </div>
  </section>

</main>
</body>
</html>
```